Wordpress Fashion Website

Please see attached:
1) Our detailed design document.
2) Velvet Lane Wardrobe logo.
3) 20 images to be used as tiles in the homepage design.
Of importance to us is:
1) That our 'Unique Selling Point' of selling fashion based on your preferred style is immediately understood by the user.
2) The site is very aesthetically pleasing and appeals to the fashion conscious woman.
3) Clean design and SEO friendly.
4) Some of the style tiles can be seen in the homepage screenshot.
The design specification document should be used as a guideline. Please use your creativity and expertise to deviate from this as you wish. We look forward to seeing your submissions!
Gareth
Updates
We very much like this design and would welcome submissions along these lines also: http://www.kemrolu.qc.ca/fr/ Added Friday, December 19, 2014
Industry/Entity Type
Fashion
Look and feel
Each slider illustrates characteristics of the customer's brand and the style your logo design should communicate.

```html
<!DOCTYPE html>
<html lang="en">
<head>
<meta charset="utf-8">
<title>Velvet Lane Wardrobe — About Us</title>
<link href="https://fonts.googleapis.com/css2?family=Roboto:wght@300;400;500&display=swap" rel="stylesheet">
<style>
  :root {
    --teal: #22aeb0;
    --teal-dark: #1f9fa1;
    --nav: #2d353a;
    --nav-line: #252c30;
    --nav-text: #5b666c;
    --footer: #222a2e;
    --footer-text: #8a9499;
    --page: #e3e3e3;
    --panel: #ffffff;
    --ink: #2b2b2b;
    --body-text: #9a9a9a;
    --rule: #e4e4e4;
  }
  * { box-sizing: border-box; margin: 0; padding: 0; }
  html, body { width: 1200px; height: 754px; overflow: hidden; }
  body {
    position: relative;
    background: var(--page);
    font-family: "Roboto", Arial, sans-serif;
    font-weight: 300;
    color: var(--ink);
  }

  /* Sidebar */
  .sidebar { position: absolute; left: 0; top: 0; width: 257px; height: 754px; background: var(--footer); box-shadow: 3px 0 8px rgba(0,0,0,.12); z-index: 2; }
  .brand { height: 184px; background: #fff; display: flex; flex-direction: column; align-items: center; justify-content: center; gap: 14px; }
  .brand-mark { width: 54px; height: 54px; border-radius: 50%; background: var(--ink); }
  .brand-name { font-weight: 400; font-size: 17px; letter-spacing: 1.5px; color: var(--ink); text-align: center; line-height: 1.25; }

  .nav { list-style: none; }
  .nav li { height: 53px; border-bottom: 1px solid var(--nav-line); background: var(--nav); display: flex; align-items: center; padding-left: 55px; font-size: 14px; text-transform: uppercase; color: var(--nav-text); }
  .nav li.active { background: var(--teal); color: #fff; border-bottom-color: var(--teal-dark); }

  .search { display: flex; height: 53px; }
  .search-field { flex: 1; background: #fff; display: flex; align-items: center; padding-left: 56px; font-size: 11px; font-style: italic; color: #a9a9a9; text-transform: uppercase; }
  .search-btn { width: 55px; background: var(--teal); display: flex; align-items: center; justify-content: center; }

  .footer { padding: 24px 0 0 48px; font-size: 10.5px; color: var(--footer-text); }
  .footer-links { margin-bottom: 16px; }
  .socials { display: flex; gap: 8px; margin-bottom: 18px; }
  .socials span { width: 20px; height: 20px; border-radius: 2px; background: #4b5a63; }
  .account { display: flex; align-items: center; gap: 6px; margin-bottom: 26px; }
  .account .login, .account .count { color: var(--teal); }
  .account svg { margin-left: 12px; }
  .legal { line-height: 18px; }

  /* Dropdown */
  .dropdown { position: absolute; left: 257px; top: 291px; width: 189px; box-shadow: 0 2px 6px rgba(0,0,0,.15); z-index: 3; font-size: 11.5px; text-transform: uppercase; }
  .dropdown div { height: 53px; display: flex; align-items: center; padding-left: 16px; }
  .dropdown .current { background: var(--nav); color: #fff; }
  .dropdown .option { background: #fff; color: var(--teal); }

  /* Main panel */
  .content { position: absolute; left: 274px; top: 17px; width: 909px; height: 720px; background: var(--panel); }
  .section-title { position: absolute; left: 26px; font-size: 16px; font-weight: 400; color: var(--ink); }
  .who-title { top: 23px; }
  .feature-frame { position: absolute; left: 26px; top: 58px; width: 415px; height: 258px; border: 1px solid #e2e2e2; padding: 5px; }
  .feature-photo { width: 100%; height: 100%; background: linear-gradient(100deg, #b9c4cc 0%, #d9d3cc 40%, #e98a6c 62%, #e7e4df 80%, #cfd4d6 100%); }
  .intro { position: absolute; left: 466px; top: 58px; width: 415px; font-size: 13.5px; line-height: 24px; color: var(--body-text); }
  .intro p + p { margin-top: 24px; }
  .divider { position: absolute; left: 26px; top: 358px; width: 857px; height: 1px; background: var(--rule); }
  .about-title { top: 420px; }
  .slider-nav { position: absolute; left: 813px; top: 402px; display: flex; gap: 1px; }
  .slider-nav span { width: 34px; height: 34px; background: var(--teal); display: flex; align-items: center; justify-content: center; }
  .styles { position: absolute; left: 26px; top: 445px; display: flex; gap: 11px; }
  .style-tile { position: relative; width: 206px; height: 189px; }
  .style-tile .photo { position: absolute; inset: 0; }
  .style-tile .label { position: absolute; left: 57px; right: 57px; top: 72px; padding-bottom: 6px; border-bottom: 1px solid #fff; text-align: center; color: #fff; font-size: 16px; }
  .boho .photo { background: linear-gradient(160deg, #6b6865, #807a73 50%, #5e5b58); }
  .casual .photo { background: linear-gradient(160deg, #5e5f61, #77777a 50%, #4f535a); }
  .chic .photo { background: linear-gradient(160deg, #6f7173, #7d6f6a 55%, #8a5f54); }
  .formal .photo { background: linear-gradient(160deg, #6a6a6b, #6f6c66 45%, #3c4d60); }
</style>
</head>
<body>
  <aside class="sidebar">
    <div class="brand">
      <span class="brand-mark"></span>
      <span class="brand-name">VELVET LANE<br>WARDROBE</span>
    </div>
    <ul class="nav">
      <li>Home</li>
      <li class="active">About Us</li>
      <li class="active">My Wordrode</li>
      <li>Editors Pics</li>
      <li>Blog</li>
      <li>Specials</li>
    </ul>
    <div class="search">
      <div class="search-field">Search your style</div>
      <div class="search-btn">
        <svg width="18" height="18" viewBox="0 0 18 18"><circle cx="7" cy="7" r="5" fill="none" stroke="#fff" stroke-width="2"/><line x1="11" y1="11" x2="16" y2="16" stroke="#fff" stroke-width="2.5" stroke-linecap="round"/></svg>
      </div>
    </div>
    <div class="footer">
      <p class="footer-links">Privacy Policy . Terms of Use . Contact Us</p>
      <div class="socials"><span></span><span></span><span></span><span></span><span></span><span></span></div>
      <p class="account">
        <span class="login">Log In</span> / <span>Sign in</span>
        <svg width="22" height="18" viewBox="0 0 22 18"><path d="M1 2h4l3 10h10l2-7H7" fill="none" stroke="#22aeb0" stroke-width="1.6"/><circle cx="9" cy="15.5" r="1.5" fill="#22aeb0"/><circle cx="17" cy="15.5" r="1.5" fill="#22aeb0"/></svg>
        <span>Shopping <span class="count">(0)</span></span>
      </p>
      <p class="legal">© 2014 Velvet Lane Wardrobe, All Rights Reserved<br>Designed &amp; Developed By Linen Pixel Studio</p>
    </div>
  </aside>

  <div class="dropdown">
    <div class="current">Search by fashion style</div>
    <div class="option">Choose your character</div>
  </div>

  <main class="content">
    <h2 class="section-title who-title">WHO ARE WE?</h2>
    <div class="feature-frame">
      <div class="feature-photo" role="img" aria-label="Woman in a coral top and pearl necklace on a city street"></div>
    </div>
    <div class="intro">
      <p>Sed non &nbsp;mauris vitae erat consequat auctor eu in elit. Class aptent taciti sociosqu ad litora torquent per conubia nostra, per inceptos himenaeos. Mauris in erat justo. Nullam ac urna eu felis dapibus condimentum sit amet a augue. Sed non neque elit. Sed ut imperdiet nisi. Proin condimentum fermentum nunc.</p>
      <p>Sed non &nbsp;mauris vitae erat consequat auctor eu in elit. Class aptent taciti sociosqu ad litora torquent per conubia nostra, per inceptos himenaeos. Mauris in erat justo. Nullam ac urna eu felis dapibus condimentum sit amet a augue. Sed non neque elit. Sed ut imperdiet nisi. Proin condimentum fermentum nunc.</p>
    </div>
    <div class="divider"></div>
    <h2 class="section-title about-title">ABOUT US</h2>
    <div class="slider-nav">
      <span><svg width="10" height="14" viewBox="0 0 10 14"><path d="M7 2L3 7l4 5" fill="none" stroke="#fff" stroke-width="2.2"/></svg></span>
      <span><svg width="10" height="14" viewBox="0 0 10 14"><path d="M3 2l4 5-4 5" fill="none" stroke="#fff" stroke-width="2.2"/></svg></span>
    </div>
    <div class="styles">
      <div class="style-tile boho"><div class="photo" role="img" aria-label="Model in a white boho dress"></div><span class="label">Boho-Chic</span></div>
      <div class="style-tile casual"><div class="photo" role="img" aria-label="Model in a tank top and jeans"></div><span class="label">Casual</span></div>
      <div class="style-tile chic"><div class="photo" role="img" aria-label="Model in a coral top"></div><span class="label">Chic</span></div>
      <div class="style-tile formal"><div class="photo" role="img" aria-label="Model in a blue strapless gown"></div><span class="label">Formal</span></div>
    </div>
  </main>
</body>
</html>
```